Business Card design
Cordavera Ruvek Martial Arts Training Center
I need single sided standard sized Business Card [3.5" x 2"]
Font in logo is CGF Locust Resistance. This font does not need to be used.
Modern
Cordavera Ruvek or Cordavera Ruvek Martial Arts Training Center
Martial Arts Discipline | Athletic Excellence
2671 Bramble Rd
Kalamazoo, MI
info@cordaverix.example
www.cordaverix.example
facebook.com/cordaverix
optional items for the business card:
Pelnor Grappling League
Todd Weslin Jiu Jitsu
Orvane Kickboxing Union
Mixed Martial Arts
Fitness
Can put the logo on one side and the information on the second side if you would like to submit that type of design.
Cordavera Ruvek illustrator file
Cordavera Ruvek eps file

```html
<!DOCTYPE html>
<html lang="en">
<head>
<meta charset="utf-8">
<title>Cordavera Ruvek — Business Card</title>
<link rel="stylesheet" href="https://fonts.googleapis.com/css2?family=Open+Sans:wght@400;600;700;800&display=swap">
<style>
  :root {
    --backdrop: #e9e9e9;
    --card-white: #ffffff;
    --card-white-shade: #f1f1f1;
    --brand-red: #ea4a3c;
    --brand-red-deep: #dc3b2e;
    --ink-gray: #5a5a5a;
    --text-light: #ffffff;
    --text-soft: rgba(255, 255, 255, 0.88);
    --divider: rgba(255, 255, 255, 0.7);
  }
  * { margin: 0; padding: 0; box-sizing: border-box; }
  html, body {
    width: 1200px;
    height: 782px;
    overflow: hidden;
    background: var(--backdrop);
    font-family: "Open Sans", Arial, sans-serif;
  }
  .canvas {
    position: relative;
    width: 1200px;
    height: 782px;
    display: flex;
    align-items: center;
    justify-content: center;
  }
  .business-card {
    width: 1000px;
    height: 572px;
    border-radius: 26px;
    overflow: hidden;
    display: flex;
    flex-direction: column;
    box-shadow: 0 10px 30px rgba(0, 0, 0, 0.18);
  }
  .card-top {
    height: 215px;
    background: linear-gradient(180deg, var(--card-white) 0%, var(--card-white-shade) 100%);
    display: flex;
    align-items: center;
    justify-content: center;
  }
  .brand-lockup {
    display: flex;
    align-items: center;
    gap: 18px;
  }
  .brand-mark {
    width: 34px;
    height: 34px;
    background: var(--brand-red);
  }
  .brand-name {
    font-size: 54px;
    font-weight: 800;
    letter-spacing: 1px;
    text-transform: uppercase;
    color: var(--ink-gray);
  }
  .card-bottom {
    flex: 1;
    background: linear-gradient(160deg, var(--brand-red) 0%, var(--brand-red-deep) 100%);
    display: flex;
    align-items: flex-start;
    padding: 52px 48px 0 60px;
    color: var(--text-light);
  }
  .identity {
    width: 430px;
    padding-top: 22px;
  }
  .identity-name {
    font-size: 40px;
    font-weight: 700;
    line-height: 1.1;
  }
  .identity-tagline {
    margin-top: 8px;
    font-size: 19px;
    font-weight: 400;
    color: var(--text-soft);
  }
  .divider {
    width: 2px;
    height: 200px;
    background: var(--divider);
    margin: 0 30px 0 10px;
  }
  .contact {
    font-size: 19px;
    font-style: normal;
    line-height: 1.55;
    color: var(--text-light);
  }
  .contact-row {
    display: flex;
  }
  .contact-label {
    width: 82px;
    font-weight: 700;
  }
  .contact-address { margin-bottom: 10px; }
</style>
</head>
<body>
  <main class="canvas">
    <article class="business-card">
      <header class="card-top">
        <div class="brand-lockup">
          <span class="brand-mark" aria-hidden="true"></span>
          <span class="brand-name">Cordavera Ruvek</span>
        </div>
      </header>
      <section class="card-bottom">
        <div class="identity">
          <h1 class="identity-name">Cordavera Ruvek</h1>
          <p class="identity-tagline">Martial Arts Discipline | Athletic Excellence</p>
        </div>
        <div class="divider" aria-hidden="true"></div>
        <address class="contact">
          <div class="contact-address">2671 Bramble Rd<br>Marlow Springs, MI 48990</div>
          <div class="contact-row"><span class="contact-label">Phone</span><span>: 269-555-0148</span></div>
          <div class="contact-row"><span class="contact-label">Cell</span><span>: 269-555-0173</span></div>
          <div class="contact-row"><span class="contact-label">Email</span><span>: info@cordaverix.example</span></div>
          <div class="contact-row"><span class="contact-label">Web</span><span>: www.cordaverix.example</span></div>
        </address>
      </section>
    </article>
  </main>
</body>
</html>
```